indépendant en tant que Massothérapeute et Préparateur Mental, j'ai besoin de ...

Massothérapeute et préparateur mental indépendant, je recherche une carte de visite sobre et dynamique, sans images liées au massage ou à la préparation mentale mais intégrant mon logo. Les couleurs que j'aime bien sont : Blanc, gris, anthracite, noir et jaune

Contact Information for Business Card

carte de préférence Horizontale
neutre qui puisse toucher le deux domaines Massothérapie et préparation mentale

Requirements
Must have
• mon projet doit intégrer au recto:
LOGO
Loïc Vermande
078 315 26 49
info@loicvermande-exemple.ch
et éventuellement www.loicvermande-exemple.ch

et au verso les deux adresses:

Chemin des Ormelets 27B
1400 Yverdon-les-Bains

Rue des Tanneries 9
1700 Fribourg

Should not have
• mon projet ne doit pas contenir d'image en liens avec le massage ni la préparation mentale.

```html
<!DOCTYPE html>
<html lang="fr">
<head>
<meta charset="utf-8">
<title>Loïc Vermande – cartes de visite</title>
<link rel="stylesheet" href="https://fonts.googleapis.com/css2?family=Montserrat:wght@400;600;700&display=swap">
<style>
  :root {
    --yellow: #fbb913;
    --black: #0d0d0d;
    --white: #ffffff;
    --stage: #2b2b2b;
    --ink: #1a1a1a;
  }
  * { margin: 0; padding: 0; box-sizing: border-box; }
  html, body { width: 1200px; height: 880px; overflow: hidden; }
  body {
    background: var(--stage);
    font-family: "Montserrat", Arial, sans-serif;
    position: relative;
  }
  .card {
    position: absolute;
    left: 280px;
    width: 640px;
    height: 360px;
    background: var(--white);
    border-radius: 22px;
    overflow: hidden;
  }
  .card--front { top: 50px; }
  .card--back { top: 470px; }
  .card__shapes { position: absolute; inset: 0; width: 100%; height: 100%; }

  .brand { position: absolute; display: flex; align-items: center; gap: 14px; }
  .brand__dot { width: 34px; height: 34px; border-radius: 50%; background: var(--black); flex: none; }
  .brand__name { font-weight: 700; font-size: 34px; color: var(--black); letter-spacing: 0.5px; line-height: 1; }
  .brand__role { font-size: 10.5px; font-weight: 600; letter-spacing: 1.4px; text-transform: uppercase; color: var(--ink); margin-top: 6px; }

  .card--front .brand { left: 130px; top: 130px; }
  .front__web {
    position: absolute; left: 0; right: 0; top: 235px; text-align: center;
    font-size: 14px; letter-spacing: 3px; color: var(--ink);
  }
  .front__web .accent { color: var(--yellow); font-weight: 600; }

  .card--back .brand { left: 150px; top: 34px; }
  .card--back .brand__name { font-size: 30px; }

  .contact { position: absolute; left: 34px; top: 180px; color: var(--white); }
  .contact__name { font-size: 24px; font-weight: 600; color: var(--yellow); margin-bottom: 10px; }
  .contact__line { display: flex; align-items: center; gap: 10px; font-size: 13px; margin-bottom: 7px; }
  .contact__line .accent { color: var(--yellow); }
  .icon-badge { width: 20px; height: 20px; border-radius: 50%; background: var(--yellow); display: flex; align-items: center; justify-content: center; flex: none; }

  .addresses { position: absolute; left: 350px; top: 150px; color: var(--ink); }
  .address { display: flex; gap: 8px; font-size: 14px; line-height: 1.3; margin-bottom: 14px; }
  .address svg { flex: none; margin-top: 3px; }

  .services {
    position: absolute; left: 0; right: 0; bottom: 8px; text-align: center;
    font-size: 15px; font-weight: 600; color: var(--ink); letter-spacing: 0.5px;
  }
</style>
</head>
<body>

<section class="card card--front" aria-label="Recto">
  <svg class="card__shapes" viewBox="0 0 640 360" aria-hidden="true">
    <polygon points="0,0 22,0 22,205 0,205" fill="var(--black)"/>
    <polygon points="0,215 30,215 95,360 0,360" fill="var(--yellow)"/>
    <polygon points="640,0 545,0 605,140 640,140" fill="var(--yellow)"/>
    <polygon points="640,148 615,148 618,360 640,360" fill="var(--black)"/>
  </svg>
  <div class="brand">
    <span class="brand__dot"></span>
    <div>
      <div class="brand__name">Loïc Vermande</div>
      <div class="brand__role">Massothérapeute / Préparateur mental</div>
    </div>
  </div>
  <p class="front__web">www.<span class="accent">loicvermande-exemple</span>.ch</p>
</section>

<section class="card card--back" aria-label="Verso">
  <svg class="card__shapes" viewBox="0 0 640 360" aria-hidden="true">
    <polygon points="0,170 300,170 318,305 0,305" fill="var(--black)"/>
    <polygon points="325,130 640,130 640,275 343,275" fill="var(--yellow)"/>
    <polygon points="0,318 640,290 640,360 0,360" fill="var(--yellow)"/>
  </svg>
  <div class="brand">
    <span class="brand__dot"></span>
    <div>
      <div class="brand__name">Loïc Vermande</div>
      <div class="brand__role">Massothérapeute / Préparateur mental</div>
    </div>
  </div>

  <div class="contact">
    <p class="contact__name">Loïc Vermande</p>
    <p class="contact__line">
      <span class="icon-badge"><svg width="11" height="11" viewBox="0 0 24 24"><path d="M6.6 10.8a15 15 0 0 0 6.6 6.6l2.2-2.2c.3-.3.7-.4 1-.2 1.1.4 2.3.6 3.6.6.6 0 1 .4 1 1V20c0 .6-.4 1-1 1A17 17 0 0 1 3 4c0-.6.4-1 1-1h3.5c.6 0 1 .4 1 1 0 1.3.2 2.5.6 3.6.1.3 0 .7-.2 1z" fill="var(--black)"/></svg></span>
      078 315 26 49
    </p>
    <p class="contact__line">
      <span class="icon-badge"><svg width="11" height="11" viewBox="0 0 24 24"><rect x="2" y="5" width="20" height="14" rx="2" fill="var(--black)"/><path d="M3 6l9 7 9-7" stroke="var(--yellow)" stroke-width="2" fill="none"/></svg></span>
      info@loicvermande-exemple.ch
    </p>
    <p class="contact__line">
      <span class="icon-badge"><svg width="12" height="12" viewBox="0 0 24 24" fill="none" stroke="var(--black)" stroke-width="2"><circle cx="12" cy="12" r="9"/><path d="M3 12h18M12 3c3 3 3 15 0 18M12 3c-3 3-3 15 0 18"/></svg></span>
      www.<span class="accent">loicvermande-exemple</span>.ch
    </p>
  </div>

  <div class="addresses">
    <p class="address">
      <svg width="12" height="16" viewBox="0 0 12 16"><path d="M6 1a5 5 0 0 0-5 5c0 4 5 9 5 9s5-5 5-9a5 5 0 0 0-5-5z" fill="none" stroke="var(--black)" stroke-width="1.6"/><circle cx="6" cy="6" r="1.8" fill="var(--black)"/></svg>
      <span>Chemin des Ormelets 27B<br>1400 Yverdon-les-Bains</span>
    </p>
    <p class="address">
      <svg width="12" height="16" viewBox="0 0 12 16"><path d="M6 1a5 5 0 0 0-5 5c0 4 5 9 5 9s5-5 5-9a5 5 0 0 0-5-5z" fill="none" stroke="var(--black)" stroke-width="1.6"/><circle cx="6" cy="6" r="1.8" fill="var(--black)"/></svg>
      <span>Rue des Tanneries 9<br>1700 Fribourg</span>
    </p>
  </div>

  <p class="services">Sports massage - Therapeutic massage - Relaxing massage</p>
</section>

</body>
</html>
```